Landing page for Cloud Kitchen buisnies

We need a landing page design fully functional for our Cloud Kitchen company wich is based in Dubai we have a industrial kitchen setup up from where we operate our own online food brands wich are only availble for delivery

Target Market(s)

Its just a company Profile

Requirements
Must have
• Company name is Ember Plate Holdings. We have the Logo already

LOGO AND DOMAIN WE HAVE
Nice to have
• Proffesionel high quality design

```html
<!DOCTYPE html>
<html lang="en">
<head>
<meta charset="utf-8">
<title>Ember Plate Holdings</title>
<link rel="stylesheet" href="https://fonts.googleapis.com/css2?family=Open+Sans:wght@300;400;600;700;800&display=swap">
<style>
:root{
  --ink:#0c1119;
  --gold:#e0bf45;
  --gold-deep:#b8892e;
  --gold-light:#f4e27a;
  --butter:#f0e07c;
  --text:#2f2f2f;
  --white:#ffffff;
}
*{margin:0;padding:0;box-sizing:border-box}
html,body{width:1200px;height:2567px;overflow:hidden}
body{font-family:"Open Sans",sans-serif;color:var(--text);background:var(--white)}
.page{position:relative;width:1200px;height:2567px;overflow:hidden;
  background:linear-gradient(#fafafa 600px,#efefef 1400px,#fff 1420px)}
.abs{position:absolute}
.gold-grad{background:linear-gradient(90deg,var(--gold-deep),var(--gold-light))}

/* hero */
.hero{left:0;top:0;width:842px;height:600px;background:var(--ink)}
.nav a{position:absolute;top:58px;font-size:12px;font-weight:600;letter-spacing:1px;color:var(--gold-deep);text-decoration:none}
.contact-btn{left:941px;top:47px;width:155px;height:39px;border-radius:20px;color:#fff;font-size:12px;font-weight:600;letter-spacing:1px;display:flex;align-items:center;justify-content:center;box-shadow:0 4px 8px rgba(0,0,0,.2)}
.brand-mark{display:flex;align-items:center;gap:10px;color:var(--gold);font-weight:700;white-space:nowrap}
.brand-mark .dot{width:14px;height:14px;border-radius:50%;background:var(--gold);flex:none}
.hero-title{left:165px;top:256px;width:345px;font-size:19px;font-weight:700;line-height:24px;color:var(--gold);letter-spacing:.6px}
.hero-copy{left:166px;top:305px;width:333px;font-size:12px;line-height:15px;font-weight:600;color:#fff;text-align:justify;letter-spacing:.55px}
.hero-photo{left:515px;top:245px;width:665px;height:400px;border-radius:48px;
  background:linear-gradient(135deg,#8a8279,#4a423b 50%,#1d1a18);box-shadow:0 0 0 6px #d9b54a}

/* about */
.section-title{left:0;width:1200px;text-align:center;font-weight:700;color:var(--gold);letter-spacing:2px}
.rule{height:1px;background:var(--gold-deep)}
.about-copy{left:220px;top:843px;width:760px;font-size:12px;line-height:15px;text-align:center;color:#444;letter-spacing:.65px}

/* offerings */
.offer-band{left:0;top:987px;width:523px;height:75px;border-radius:0 38px 38px 0;color:#fff;font-size:42px;font-weight:700;letter-spacing:2px;padding-left:130px;line-height:75px;box-shadow:0 6px 10px rgba(0,0,0,.15)}
.offer-art{width:160px;height:125px;border-radius:60px 70px 20px 20px;background:linear-gradient(135deg,#f1d85e,#c7a03a 55%,#2b35a8)}
.offer-title{width:240px;text-align:center;font-size:16px;font-weight:700;letter-spacing:1px;color:var(--gold)}
.offer-copy{width:232px;font-size:12px;line-height:15px;text-align:justify;text-align-last:center;color:#444;letter-spacing:.45px}
.offer-line{width:1px;height:24px;background:#bbb}

/* why us */
.scallops{left:-20px;top:1410px}
.why-photo{left:219px;top:1394px;width:274px;height:412px;background:linear-gradient(160deg,#d8d6d2,#6a6560 55%,#2a2826)}
.why-block{left:154px;top:1483px;width:65px;height:302px;background:var(--butter)}
.why-title{left:695px;top:1468px;width:196px;text-align:center;font-size:40px;font-weight:700;color:var(--gold);letter-spacing:2px;line-height:52px}
.why-item{left:709px;width:256px;font-size:12px;line-height:15px;font-weight:700;color:#333;text-align:justify;letter-spacing:.3px}
.tick{left:636px}

/* brands */
.brand-tile{width:150px;height:100px;display:flex;align-items:center;justify-content:center}
.brand-tile span{font-size:16px;font-weight:700;color:var(--gold-deep);text-align:center;line-height:20px}

/* signup */
.signup{left:355px;top:2235px;width:490px;height:55px;border-radius:28px;background:#fff;box-shadow:0 4px 10px rgba(0,0,0,.15);overflow:hidden;z-index:2}
.signup .email{position:absolute;left:77px;top:0;line-height:55px;font-size:16px;color:#444}
.signup .submit{position:absolute;left:285px;top:0;width:205px;height:55px;color:#fff;font-size:24px;font-weight:700;letter-spacing:2px;text-align:center;line-height:55px}

/* footer */
.footer{left:0;top:2263px;width:1200px;height:304px;background:var(--ink)}
.footer-line{left:455px;font-size:17px;color:#fff;letter-spacing:.5px;display:flex;align-items:center;gap:10px}
.copyright{left:0;top:2509px;width:1200px;text-align:center;color:var(--gold);font-size:17px;letter-spacing:.3px}
</style>
</head>
<body>
<svg width="0" height="0" style="position:absolute" aria-hidden="true">
  <defs>
    <linearGradient id="goldStroke" x1="0" y1="1" x2="1" y2="0">
      <stop offset="0" stop-color="#b8892e"/>
      <stop offset="1" stop-color="#f4e27a"/>
    </linearGradient>
  </defs>
</svg>
<div class="page">

  <!-- hero -->
  <div class="abs hero"></div>
  <nav class="nav">
    <a style="left:414px">ABOUT US</a>
    <a style="left:555px">OUR OFFERINGS</a>
    <a style="left:736px">WHY US</a>
  </nav>
  <div class="abs contact-btn gold-grad">CONTACT US</div>
  <div class="abs brand-mark" style="left:165px;width:320px;justify-content:center;top:140px;font-size:20px"><span class="dot"></span>Ember Plate Holdings</div>
  <h1 class="abs hero-title">QUALITY COMMERCIAL KITCHEN OPTIMIZED FOR DELIVERY.</h1>
  <p class="abs hero-copy">Lorem ipsum dolor sit amet, consectetur adipisicing elit, sed do eiusmod tempor incididunt ut labore et dolore magna aliqua. Ut enim ad minim veniam, quis nostrud exercitation ullamco laboris nisi ut aliquip ex ea commodo consequat. Duis aute irure dolor in reprehenderit in voluptate velit esse cillum dolore eu fugiat nulla pariatur. Excepteur sint occaecat cupidatat non proident, sunt in culpa qui officia deserunt mollit anim id est laborum.</p>

  <div class="abs hero-photo" role="img" aria-label="Photo of a chef working in a commercial kitchen"></div>

  <!-- about -->
  <h2 class="abs section-title" style="top:716px;font-size:42px">WHAT IS EMBER PLATE</h2>
  <div class="abs rule" style="left:356px;top:792px;width:161px"></div>
  <div class="abs section-title" style="top:776px;font-size:24px;font-weight:300">ABOUT US</div>
  <div class="abs rule" style="left:685px;top:792px;width:162px"></div>
  <p class="abs about-copy">Lorem ipsum dolor sit amet, consectetur adipisicing elit, sed do eiusmod tempor incididunt ut labore et dolore magna aliqua. Ut enim ad minim veniam, quis nostrud exercitation ullamco laboris nisi ut aliquip ex ea commodo consequat. Duis aute irure dolor in reprehenderit in voluptate velit esse cillum dolore eu fugiat nulla pariatur. Excepteur sint occaecat cupidatat non proident, sunt in culpa qui officia deserunt mollit anim id est laborum.</p>

  <!-- offerings -->
  <h2 class="abs offer-band gold-grad">OUR OFFERINGS</h2>

  <div class="abs offer-art" style="left:164px;top:1112px" role="img" aria-label="Illustration of a person ordering food on a tablet"></div>
  <div class="abs offer-art" style="left:520px;top:1112px" role="img" aria-label="Illustration of a covered serving dish among plants"></div>
  <div class="abs offer-art" style="left:875px;top:1112px" role="img" aria-label="Illustration of a delivery scooter with a timer"></div>

  <div class="abs offer-line" style="left:125px;top:1266px"></div>
  <h3 class="abs offer-title" style="left:124px;top:1265px">LOREM IPSUM</h3>
  <p class="abs offer-copy" style="left:128px;top:1292px">Lorem ipsum dolor sit amet, consectetur adipiscing elit, sed do eiusmod tempor incididunt ut labore et dolore magna aliqua. Quis ipsum suspendisse ultrices gravida.</p>

  <div class="abs offer-line" style="left:481px;top:1266px"></div>
  <h3 class="abs offer-title" style="left:480px;top:1265px">LOREM IPSUM</h3>
  <p class="abs offer-copy" style="left:484px;top:1292px">Lorem ipsum dolor sit amet, consectetur adipiscing elit, sed do eiusmod tempor incididunt ut labore et dolore magna aliqua. Quis ipsum suspendisse ultrices gravida.</p>

  <div class="abs offer-line" style="left:836px;top:1266px"></div>
  <h3 class="abs offer-title" style="left:835px;top:1265px">LOREM IPSUM</h3>
  <p class="abs offer-copy" style="left:839px;top:1292px">Lorem ipsum dolor sit amet, consectetur adipiscing elit, sed do eiusmod tempor incididunt ut labore et dolore magna aliqua. Quis ipsum suspendisse ultrices gravida.</p>

  <!-- why us -->
  <svg class="abs scallops" width="1240" height="60" viewBox="0 0 1240 60" aria-hidden="true">
    <g fill="#fff">
      <circle cx="50" cy="45" r="34"/><circle cx="110" cy="50" r="28"/><circle cx="170" cy="45" r="34"/><circle cx="230" cy="50" r="28"/>
      <circle cx="290" cy="45" r="34"/><circle cx="350" cy="50" r="28"/><circle cx="410" cy="45" r="34"/><circle cx="470" cy="50" r="28"/>
      <circle cx="530" cy="45" r="34"/><circle cx="590" cy="50" r="28"/><circle cx="650" cy="45" r="34"/><circle cx="710" cy="50" r="28"/>
      <circle cx="770" cy="45" r="34"/><circle cx="830" cy="50" r="28"/><circle cx="890" cy="45" r="34"/><circle cx="950" cy="50" r="28"/>
      <circle cx="1010" cy="45" r="34"/><circle cx="1070" cy="50" r="28"/><circle cx="1130" cy="45" r="34"/><circle cx="1190" cy="50" r="28"/>
      <rect x="0" y="45" width="1240" height="15"/>
    </g>
  </svg>
  <div class="abs why-block"></div>
  <div class="abs why-photo" role="img" aria-label="Photo of a gloved cook seasoning a steel bowl"></div>

  <div class="abs rule" style="left:620px;top:1494px;width:75px"></div>
  <h2 class="abs why-title">WHY US</h2>
  <div class="abs rule" style="left:891px;top:1494px;width:75px"></div>

  <svg class="abs tick" style="top:1550px" width="42" height="34" viewBox="0 0 42 34" aria-hidden="true"><path d="M2 18 L14 30 L40 2 L14 22 Z" fill="url(#goldStroke)"/></svg>
  <p class="abs why-item" style="top:1540px">Lorem ipsum dolor sit amet, consectetur adipiscing elit, sed do eiusmod tempor incididunt ut labore et dolore magna aliqua.</p>
  <svg class="abs tick" style="top:1640px" width="42" height="34" viewBox="0 0 42 34" aria-hidden="true"><path d="M2 18 L14 30 L40 2 L14 22 Z" fill="url(#goldStroke)"/></svg>
  <p class="abs why-item" style="top:1630px">Lorem ipsum dolor sit amet, consectetur adipiscing elit, sed do eiusmod tempor incididunt ut labore et dolore magna aliqua.</p>
  <svg class="abs tick" style="top:1730px" width="42" height="34" viewBox="0 0 42 34" aria-hidden="true"><path d="M2 18 L14 30 L40 2 L14 22 Z" fill="url(#goldStroke)"/></svg>
  <p class="abs why-item" style="top:1720px">Lorem ipsum dolor sit amet, consectetur adipiscing elit, sed do eiusmod tempor incididunt ut labore et dolore magna aliqua.</p>

  <!-- brands -->
  <h2 class="abs section-title" style="top:1894px;font-size:42px">OUR BRANDS</h2>
  <div class="abs brand-tile" style="left:174px;top:1980px"><span>Ember Plate Holdings</span></div>
  <div class="abs brand-tile" style="left:354px;top:1980px"><span>Ember Plate Holdings</span></div>
  <div class="abs brand-tile" style="left:535px;top:1980px"><span>Ember Plate Holdings</span></div>
  <div class="abs brand-tile" style="left:715px;top:1980px"><span>Ember Plate Holdings</span></div>
  <div class="abs brand-tile" style="left:895px;top:1980px"><span>Ember Plate Holdings</span></div>

  <!-- updates -->
  <div class="abs rule" style="left:384px;top:2190px;width:72px"></div>
  <h2 class="abs section-title" style="top:2175px;font-size:24px">GET OUR UPDATES</h2>
  <div class="abs rule" style="left:746px;top:2190px;width:71px"></div>

  <div class="abs footer"></div>
  <form class="abs signup">
    <svg style="position:absolute;left:29px;top:19px" width="28" height="18" viewBox="0 0 28 18" aria-hidden="true"><rect width="28" height="18" fill="#bbb"/><path d="M0 0 L14 10 L28 0" fill="none" stroke="#fff" stroke-width="2"/></svg>
    <span class="email">Your Email...</span>
    <span class="submit gold-grad">SUBMIT</span>
  </form>

  <!-- footer -->
  <div class="abs brand-mark" style="left:183px;top:2405px;font-size:20px"><span class="dot"></span>Ember Plate Holdings</div>
  <div class="abs footer-line" style="top:2370px">
    <svg width="26" height="30" viewBox="0 0 26 30" aria-hidden="true"><path d="M6 2 L11 8 L8 12 C10 17 13 21 17 23 L21 20 L25 26 L20 29 C10 27 2 16 2 6 Z" fill="url(#goldStroke)"/></svg>
    <span>+123 456 7890</span>
  </div>
  <div class="abs footer-line" style="top:2430px">
    <svg width="28" height="28" viewBox="0 0 28 28" aria-hidden="true"><circle cx="14" cy="14" r="14" fill="url(#goldStroke)"/><text x="14" y="19" text-anchor="middle" font-size="15" font-family="Open Sans, sans-serif" fill="#0c1119">@</text></svg>
    <span>contact@emberplateholdings.com</span>
  </div>
  <p class="abs copyright">© 2020 EMBER PLATE HOLDINGS | ALL RIGHTS RESERVED</p>
</div>
</body>
</html>
```